Belford & Company

We are a boutique commercial real estate firm. For our Business card design - sleek, modern, yet high-end/classy. Please see our website: belfordandcompany.example for details.

We currently need 2 business card names and the ability to add/change the business card information -
Name, Title, Address, Office #, Mobile #, Fax, Email and company website.

Industry/Entity Type

Real Estate

Contact Information for Business Card

Business card design - sleek, modern, yet high-end/classy. Please see our website: belfordandcompany.example for details.

Also, we'd like to have our slogan "Dedication Defines The Outcome." somewhere in there. We'd like to make some part of it raised or a different texture if possible.
Color #'s:
blue 19 36 128
light gray 222 222 221
dark gray 107 120 128

Also, we'd like to have our slogan "Dedication Defines The Outcome." somewhere in there. We'd like to make some part of it raised or a different texture if possible - grey on one side and blue on the other - rounded edges preferred. Maybe either metal/silver/grey raised logo on the back. Thank you!!

Requirements
Must have
• Sleek, modern, clean and classy design

```html
<!DOCTYPE html>
<html lang="en">
<head>
<meta charset="utf-8">
<title>Belford &amp; Company — Business Card</title>
<link rel="stylesheet" href="https://fonts.googleapis.com/css2?family=Montserrat:wght@400;500;600;700&display=swap">
<style>
  :root {
    --brand-blue: #132480;
    --brand-gray: #6b7880;
    --light-gray: #dededd;
    --canvas: #e9e9e9;
    --white: #ffffff;
    --soft-white: #e6e8f2;
  }
  * { margin: 0; padding: 0; box-sizing: border-box; }
  html, body { width: 1200px; height: 800px; overflow: hidden; }
  body {
    background: var(--canvas);
    font-family: "Montserrat", sans-serif;
    color: var(--white);
    position: relative;
  }
  .card {
    position: absolute;
    top: 278px;
    width: 420px;
    height: 240px;
    border-radius: 2px;
  }
  .card-front { left: 141px; background: var(--brand-gray); }
  .card-back { left: 637px; background: var(--brand-blue); }

  /* Front */
  .front-name {
    position: absolute;
    left: 0; right: 0;
    top: 54px;
    text-align: center;
    font-weight: 700;
    line-height: 1.08;
    letter-spacing: 1px;
  }
  .front-name .line-1 { display: block; font-size: 50px; }
  .front-name .line-2 { display: block; font-size: 34px; }
  .front-rule {
    position: absolute;
    left: 114px; right: 114px;
    top: 164px;
    height: 2px;
    background: var(--white);
  }
  .front-tagline {
    position: absolute;
    left: 0; right: 0;
    top: 170px;
    text-align: center;
    font-size: 12.5px;
    font-weight: 600;
    letter-spacing: 3.4px;
  }

  /* Back */
  .brand-block {
    position: absolute;
    right: 28px;
    top: 44px;
    text-align: right;
  }
  .brand-name {
    font-size: 17px;
    font-weight: 700;
    line-height: 1.1;
    letter-spacing: 0.5px;
  }
  .brand-descriptor {
    margin-top: 4px;
    font-size: 9px;
    font-weight: 600;
    letter-spacing: 2.4px;
  }
  .slogan {
    position: absolute;
    right: 28px;
    top: 98px;
    font-size: 8px;
    font-weight: 600;
    letter-spacing: 0.8px;
  }
  .person {
    position: absolute;
    left: 28px;
    top: 78px;
  }
  .person-name { font-size: 15.5px; font-weight: 600; letter-spacing: 0.6px; line-height: 1.1; }
  .person-title { font-size: 11.5px; font-weight: 400; color: var(--soft-white); }
  .divider {
    position: absolute;
    left: 28px; right: 28px;
    top: 118px;
    height: 1px;
    background: rgba(255,255,255,0.55);
  }
  .contact-list {
    position: absolute;
    left: 28px;
    top: 133px;
    list-style: none;
    font-size: 12.5px;
    line-height: 16px;
  }
  .contact-list li { display: flex; align-items: center; gap: 7px; }
  .contact-list .gap-top { margin-top: 3px; }
  .icon { width: 11px; height: 11px; fill: var(--white); flex: none; }
  .address {
    position: absolute;
    right: 28px;
    top: 133px;
    display: flex;
    gap: 7px;
    font-size: 12.5px;
    line-height: 16px;
    text-align: right;
  }
  .address .icon { margin-top: 3px; }
</style>
</head>
<body>

  <section class="card card-front" aria-label="Card front">
    <div class="front-name">
      <span class="line-1">BELFORD</span>
      <span class="line-2">&amp; COMPANY</span>
    </div>
    <div class="front-rule"></div>
    <div class="front-tagline">REALTY ADVISORS</div>
  </section>

  <section class="card card-back" aria-label="Card back">
    <div class="person">
      <div class="person-name">DANIEL HARTLEY</div>
      <div class="person-title">Your Title</div>
    </div>

    <div class="brand-block">
      <div class="brand-name">BELFORD<br>&amp; COMPANY</div>
      <div class="brand-descriptor">REALTY ADVISORS</div>
    </div>
    <div class="slogan">DEDICATION DEFINES THE OUTCOME</div>

    <div class="divider"></div>

    <ul class="contact-list">
      <li>
        <svg class="icon" viewBox="0 0 12 12" aria-hidden="true"><circle cx="6" cy="6" r="6"/><path d="M4 3.2l1 1.6-.6.7c.4.8 1 1.4 1.8 1.8l.7-.6 1.6 1-.5 1.2C6 8.8 3.2 6 3 4z" fill="#132480"/></svg>
        555 210 4433
      </li>
      <li>
        <svg class="icon" viewBox="0 0 12 12" aria-hidden="true"><circle cx="6" cy="6" r="6"/><rect x="4.2" y="2.6" width="3.6" height="6.8" rx="0.6" fill="#132480"/><rect x="4.9" y="3.4" width="2.2" height="4.4" fill="#fff"/></svg>
        555 318 4566
      </li>
      <li>
        <svg class="icon" viewBox="0 0 12 12" aria-hidden="true"><rect x="0.5" y="4" width="11" height="7.5" rx="1"/><rect x="3" y="0.5" width="6" height="4"/><rect x="3" y="6" width="6" height="1" fill="#132480"/><rect x="3" y="8" width="6" height="1" fill="#132480"/></svg>
        555 426 4566
      </li>
      <li class="gap-top">
        <svg class="icon" viewBox="0 0 12 12" aria-hidden="true"><rect x="0.5" y="2" width="11" height="8" rx="0.8"/><path d="M1 2.6L6 6.6l5-4" fill="none" stroke="#132480" stroke-width="1"/></svg>
        info@belfordandcompany.example
      </li>
      <li>
        <svg class="icon" viewBox="0 0 12 12" aria-hidden="true"><circle cx="6" cy="6" r="5.6"/><g fill="none" stroke="#132480" stroke-width="0.8"><ellipse cx="6" cy="6" rx="2.4" ry="5.6"/><path d="M0.6 6h10.8M1.4 3.5h9.2M1.4 8.5h9.2"/></g></svg>
        www.belfordandcompany.example
      </li>
    </ul>

    <div class="address">
      <div>2285 Harbor View Rd., Suite #310<br>Port Alder, FL 30000</div>
      <svg class="icon" viewBox="0 0 12 12" aria-hidden="true"><path d="M6 0.5a4 4 0 0 0-4 4c0 3 4 7 4 7s4-4 4-7a4 4 0 0 0-4-4z"/><circle cx="6" cy="4.5" r="1.5" fill="#132480"/></svg>
    </div>
  </section>

</body>
</html>
```